Verdant Loop Advisors, LLC

I am looking for a simple, clear layout with my logo prominent and embossed, on the best quality card stock available. I would like the business name and phone number included on the card as well......I dont want my name anywhere on the card and I would like my logo embossed on the card......something simple with a white back......open to designs as long as they go along with recycling symbols and green type stuff.....The address, website, cell number, fax number, and email are listed below

5374 Tillbury Fenwood Road
Hyattsville, MD 20785

c. 240.555.0143 f. 240.555.0187
e. sales@verdantloopadvisors.example
w. www.verdantloopadvisors.example

Industry/Entity Type

Recycling

```html
<!DOCTYPE html>
<html lang="en">
<head>
<meta charset="utf-8">
<title>Verdant Loop Advisors, LLC — Business Card</title>
<link rel="stylesheet" href="https://fonts.googleapis.com/css2?family=Arimo:wght@400;700&display=swap">
<style>
  :root {
    --green: #2f6b3f;
    --green-dark: #1f5a32;
    --green-light: #7fa98a;
    --charcoal: #3a3839;
    --paper: #ffffff;
    --mist: #e8f0e3;
  }
  * { margin: 0; padding: 0; box-sizing: border-box; }
  html, body { width: 1200px; height: 720px; overflow: hidden; background: var(--paper); }
  .card {
    position: relative;
    width: 1200px;
    height: 720px;
    background: var(--paper);
    font-family: "Arimo", Arial, sans-serif;
  }
  .backdrop-art {
    position: absolute;
    left: 372px;
    top: 94px;
    width: 450px;
    height: 430px;
    border-radius: 50%;
    background: radial-gradient(circle at 50% 50%, var(--mist) 0%, rgba(232,240,227,0.6) 45%, rgba(255,255,255,0) 72%);
  }
  .brand {
    position: absolute;
    left: 96px;
    top: 298px;
    display: flex;
    align-items: center;
    gap: 18px;
  }
  .brand-mark {
    width: 62px;
    height: 62px;
    background: var(--green);
  }
  .brand-name {
    font-size: 33px;
    font-weight: 700;
    color: var(--charcoal);
    letter-spacing: 0.5px;
    white-space: nowrap;
  }
  .divider {
    position: absolute;
    left: 725px;
    top: 298px;
    width: 7px;
    height: 79px;
    background: var(--green-dark);
  }
  .address {
    position: absolute;
    left: 752px;
    top: 298px;
    font-size: 27px;
    line-height: 38px;
    color: var(--green-dark);
    font-style: normal;
    letter-spacing: -0.3px;
  }
  .rule {
    position: absolute;
    left: 0;
    top: 532px;
    width: 1200px;
    height: 7px;
    background: linear-gradient(90deg, var(--green-dark) 0%, var(--green) 40%, var(--green-light) 55%, var(--green) 70%, var(--green-dark) 100%);
  }
  .contact-list {
    position: absolute;
    top: 560px;
    list-style: none;
  }
  .contact-list.phones { left: 155px; }
  .contact-list.online { left: 634px; }
  .contact-item {
    display: flex;
    align-items: center;
    gap: 10px;
    height: 38px;
    font-size: 27px;
    color: var(--green-dark);
    letter-spacing: -0.3px;
  }
  .contact-icon { width: 30px; height: 24px; flex: none; }
</style>
</head>
<body>
<main class="card">
  <div class="backdrop-art" role="img" aria-label="Faint recycling arrows circling a globe"></div>

  <div class="brand">
    <div class="brand-mark" aria-hidden="true"></div>
    <div class="brand-name">Verdant Loop Advisors, LLC</div>
  </div>

  <div class="divider" aria-hidden="true"></div>
  <address class="address">
    5374 Tillbury Fenwood Road<br>
    Hyattsville, MD 20785
  </address>

  <div class="rule" aria-hidden="true"></div>

  <ul class="contact-list phones">
    <li class="contact-item">
      <svg class="contact-icon" viewBox="0 0 30 24" aria-label="Cell">
        <path d="M8 3 C5 4 4 7 6 11 C8 15 12 19 17 21 C20 22 22 20 23 18 L19 15 L16 17 C13 15 11 13 10 10 L12 7 Z" fill="var(--green)"/>
      </svg>
      <span>240.555.0143</span>
    </li>
    <li class="contact-item">
      <svg class="contact-icon" viewBox="0 0 30 24" aria-label="Fax">
        <rect x="9" y="2" width="12" height="8" fill="none" stroke="var(--green)" stroke-width="2"/>
        <rect x="4" y="9" width="22" height="11" rx="2" fill="var(--green)"/>
        <rect x="9" y="15" width="12" height="7" fill="#fff" stroke="var(--green)" stroke-width="2"/>
      </svg>
      <span>240.555.0187</span>
    </li>
  </ul>

  <ul class="contact-list online">
    <li class="contact-item">
      <svg class="contact-icon" viewBox="0 0 30 24" aria-label="Email">
        <rect x="2" y="4" width="26" height="17" fill="none" stroke="var(--green)" stroke-width="2"/>
        <path d="M3 5 L15 14 L27 5" fill="none" stroke="var(--green)" stroke-width="2"/>
      </svg>
      <span>sales@verdantloopadvisors.example</span>
    </li>
    <li class="contact-item">
      <svg class="contact-icon" viewBox="0 0 30 24" aria-label="Website">
        <circle cx="15" cy="12" r="10" fill="none" stroke="var(--green)" stroke-width="2"/>
        <ellipse cx="15" cy="12" rx="4.5" ry="10" fill="none" stroke="var(--green)" stroke-width="1.6"/>
        <line x1="5" y1="12" x2="25" y2="12" stroke="var(--green)" stroke-width="1.6"/>
      </svg>
      <span>www.verdantloopadvisors.example</span>
    </li>
  </ul>
</main>
</body>
</html>
```